Strength Coach Business Card Design Project

I would like a business card design to complement my new logo. I would like the card to be clean, seek and strong!

Target Market(s)

Mostly adults and junior atheletes who are serious about changing their lives.

Industry/Entity Type

Business

Font styles to use
Serif

Colors

Designer to choose colors to be used in the design.

```html
<!DOCTYPE html>
<html lang="en">
<head>
<meta charset="utf-8">
<title>Ridge Strength &amp; Fitness – Business Card</title>
<link href="https://fonts.googleapis.com/css2?family=Tinos:wght@400;700&display=swap" rel="stylesheet">
<style>
  :root {
    --stage: #e9e7e3;
    --paper: #ffffff;
    --accent-red: #e21f2b;
    --band-grey-dark: #363636;
    --band-grey-light: #7b7b7b;
    --ink: #161616;
    --brand-ink: #404040;
    --figure: #333333;
  }
  html, body {
    margin: 0;
    width: 1200px;
    height: 800px;
    overflow: hidden;
    background: var(--stage);
  }
  .card {
    position: absolute;
    left: 75px;
    top: 100px;
    width: 1050px;
    height: 600px;
    background: var(--paper);
    box-shadow: 0 10px 30px rgba(0,0,0,0.18);
  }
  .card svg { display: block; }
  .serif { font-family: "Tinos", "Times New Roman", serif; }
  .brand-name { fill: var(--brand-ink); font-weight: 700; }
  .holder-name { fill: #ffffff; font-weight: 700; font-size: 30px; letter-spacing: 2px; }
  .holder-role { fill: #ffffff; font-size: 24px; }
  .contact-line { fill: var(--ink); font-size: 21px; }
  .icon { fill: var(--accent-red); }
  .icon-stroke { fill: none; stroke: var(--accent-red); stroke-width: 2; }
</style>
</head>
<body>
<div class="card">
  <svg width="1050" height="600" viewBox="0 0 1050 600" xmlns="http://www.w3.org/2000/svg">
    <defs>
      <linearGradient id="greyBand" x1="0" y1="0" x2="1" y2="0">
        <stop offset="0" stop-color="var(--band-grey-dark)"/>
        <stop offset="1" stop-color="var(--band-grey-light)"/>
      </linearGradient>
    </defs>

    <!-- diagonal bands -->
    <polygon class="band-grey" points="0,245 1050,445 1050,540 0,540" fill="url(#greyBand)"/>
    <polygon class="band-red" points="0,195 1050,395 1050,445 0,245" fill="var(--accent-red)"/>

    <!-- athlete figure area -->
    <rect class="athlete-figure" role="img" aria-label="Silhouette of a flexing bodybuilder"
          x="230" y="40" width="270" height="300" rx="60" fill="var(--figure)"/>

    <!-- brand name -->
    <g class="brand">
      <rect x="640" y="140" width="30" height="30" fill="var(--accent-red)"/>
      <text class="serif brand-name" x="690" y="170" font-size="52">RIDGE</text>
      <text class="serif brand-name" x="690" y="205" font-size="24" letter-spacing="1">STRENGTH &amp; FITNESS</text>
    </g>

    <!-- name on red band -->
    <g class="holder" transform="rotate(10.8 560 320)">
      <text class="serif holder-name" x="500" y="343">MARCUS VALE</text>
      <line x1="755" y1="318" x2="755" y2="350" stroke="#ffffff" stroke-width="2"/>
      <text class="serif holder-role" x="775" y="343">Managing Director</text>
    </g>

    <!-- contact details -->
    <g class="contacts serif" text-anchor="end">
      <text class="contact-line" x="970" y="450">0044 7812 305</text>
      <text class="contact-line" x="970" y="476">info@ridgestrength.com</text>
      <text class="contact-line" x="970" y="502">www.ridgestrength.com</text>
      <text class="contact-line" x="970" y="528">Studio 4, 18 Harbor Road, Fairview, NJ 07022</text>
    </g>

    <!-- contact icons -->
    <g class="contact-icons">
      <path class="icon" d="M984 446 h18 v-4 a3 3 0 0 0 -3 -3 h-12 a3 3 0 0 0 -3 3 z M986 447 h14 l2 6 h-18 z"/>
      <rect class="icon-stroke" x="984" y="462" width="18" height="13"/>
      <polyline class="icon-stroke" points="984,462 993,470 1002,462"/>
      <rect class="icon-stroke" x="984" y="487" width="18" height="12"/>
      <line class="icon-stroke" x1="990" y1="502" x2="996" y2="502"/>
      <path class="icon" d="M993 510 l10 9 h-3 v8 h-5 v-5 h-4 v5 h-5 v-8 h-3 z"/>
    </g>
  </svg>
</div>
</body>
</html>
```